Become the head packaging designer of Tolvenu: Desing our vacuumbag packaging

Become the head designer of Tolvenu. A new brand of household products.

BRAND:
Tolvenu is our new brand which consists of accessories and spareparts of home appliances. These are products like vacuumbags, descalers, toothbrush heads, waterfilters for your frigde. So a lot of products that are consumed by household appliances. Tolvenu is positioned as being 'good quality, fair prices' (best buy). Important aspect is that the packaging should communicate that the products are of high quality. Most products are alternatives to original products so therefore the customer should be convinced they are buying products of the same or better quality as the original, but for better prices.

PRODUCT:
The first productline we are going to introduce is vacuumbags. These are alternative to the original bags of the manufacturer. The market position is 'good quality, low prices' (best buy). Details further below.

FUTURE DESIGNS:
We want to consider the winner as our packaging designer if we can agree on a fair price and if we're in line concerning the designs. That is why I want to consider the vacuumbags as a pilot.

DETAILS FOR THIS DESIGN:
- It will be several different bags (about 8) which are designed for different vacuumcleaners. Goal is to have one universal design with some variable elements we can adjust ourselves.
- The bags will be packaged by 4 pieces and will be in a plastic sealed bag. On this plastic bag will be a A5-sticker in colors with the design on it.
- The design should be a fresh, clear design and fitting for the target audience and market position.
- The elements which should be on there are:
(1) Our logo
(2) Pictures with text of aspects of the bags: super hygienic, high performance (good sucking power of vacuumcleaner), microfibre quality, 2x durability (can be used two times a standard paper vacuumbag can be used)
(3) Picture of microfibre vacuumbags
(4) Number of bags in packaging: 4
(5) Brandname(s) (for which the vacuumbag is suited. f.e. Korpa, KTR, Fenlo). - VARIABLE
(6) QR code - VARIABLE
(7) SKU (articlenumber) - VARIABLE
(8) Barcode - VARIABLE

Comparable product(s) (NOT for design):
http://www.tramvel.nl/nl/trmnl/huishoudelijk-en-schoonmaak/stofzuigerzakken/korvest/kv42-duraweefplus-stofzuigerzakken
http://www.durap.nl/winkel/huis-en-tuin/huis/huishoudelijk/stofzuigers/stofzuigerzakken-korvest-q-zak-(48213976)
http://www.zakkenwinkelier.com/ktr-vm-24-37.html

Target Market(s)

Typical households. B2C (end-consumers).

Requirements
Must have
• Quality, fresh, distinctive design.
Should not have
• Old-fashioned or cheap feeling.

```html
<!DOCTYPE html>
<html lang="en">
<head>
<meta charset="utf-8">
<title>Tolvenu vacuum bag packaging</title>
<link rel="stylesheet" href="https://fonts.googleapis.com/css2?family=Montserrat:wght@400;500;700&display=swap">
<style>
  :root {
    --brand-red: #e52a2d;
    --brand-red-soft: #ef5a5c;
    --ink-white: #ffffff;
    --outline: #5a5a5a;
    --page: #ffffff;
  }
  * { margin: 0; padding: 0; box-sizing: border-box; }
  html, body {
    width: 744px;
    height: 1200px;
    overflow: hidden;
    background: var(--page);
  }
  .canvas {
    position: relative;
    width: 744px;
    height: 1200px;
    font-family: "Montserrat", Arial, sans-serif;
    color: var(--ink-white);
  }
  .hang-tab {
    position: absolute;
    left: 0;
    top: 0;
    width: 744px;
    height: 176px;
  }
  .package {
    position: absolute;
    left: 38px;
    top: 172px;
    width: 668px;
    height: 946px;
    background: var(--brand-red);
    border: 1.5px solid var(--outline);
  }
  .brand-name {
    position: absolute;
    left: 28px;
    top: 56px;
    font-weight: 700;
    font-size: 50px;
    line-height: 1;
    letter-spacing: 0.5px;
  }
  .intro-copy {
    position: absolute;
    left: 28px;
    top: 172px;
    font-size: 17px;
    font-weight: 400;
    line-height: 25px;
  }
  .features {
    position: absolute;
    left: 28px;
    top: 458px;
    display: flex;
    align-items: center;
    gap: 16px;
  }
  .feature-label {
    text-align: center;
    font-size: 16px;
    font-weight: 500;
    line-height: 20px;
    width: 112px;
  }
  .feature-dots {
    display: flex;
    justify-content: center;
    gap: 6px;
    margin-top: 8px;
  }
  .feature-dots span {
    width: 5px;
    height: 5px;
    border-radius: 50%;
    background: var(--ink-white);
  }
  .bag-visual {
    position: absolute;
    left: 49px;
    top: 632px;
    width: 445px;
    height: 190px;
    background: linear-gradient(135deg, var(--brand-red-soft), var(--brand-red));
    border-radius: 4px;
  }
</style>
</head>
<body>
<main class="canvas">
  <svg class="hang-tab" viewBox="0 0 744 176" aria-hidden="true">
    <path d="M99 174 L235 12 L507 12 L656 174 Z" fill="var(--brand-red)" stroke="var(--outline)" stroke-width="1.5"/>
    <circle cx="372" cy="111" r="12" fill="var(--page)" stroke="var(--outline)" stroke-width="1.5"/>
  </svg>

  <section class="package">
    <div class="brand-name">Tolvenu</div>

    <p class="intro-copy">
      Lorem ipsum dolor sit amet<br>
      consectetur adipiscing elit, sed do eiusmo<br>
      ut labore et dolore magna aliqua<br>
      ct enim ad minim veniam<br>
      quis nostrud exercitation ullamco laboris<br>
      nisi ut aliquip ex ea commodo consequat
    </p>

    <div class="features">
      <div class="feature-label">
        Microfibre<br>Quality
        <div class="feature-dots"><span></span><span></span><span></span><span></span></div>
      </div>
      <svg width="58" height="58" viewBox="0 0 58 58" aria-label="Microfibre quality icon">
        <circle cx="29" cy="29" r="26" fill="none" stroke="var(--ink-white)" stroke-width="2"/>
        <path d="M17 35 L35 17 M21 40 L40 21 M26 44 L44 26" stroke="var(--ink-white)" stroke-width="2" stroke-linecap="round"/>
      </svg>
      <svg width="64" height="64" viewBox="0 0 64 64" aria-label="Four bags">
        <circle cx="32" cy="32" r="29" fill="none" stroke="var(--ink-white)" stroke-width="2"/>
        <text x="32" y="41" text-anchor="middle" fill="var(--ink-white)" font-family="Montserrat, Arial, sans-serif" font-size="24" font-weight="500">4X</text>
      </svg>
    </div>

    <div class="bag-visual" role="img" aria-label="Outline illustration of a microfibre vacuum bag"></div>
  </section>
</main>
</body>
</html>
```